ZMobvra - Tenant Place Services

Want Quality Tenants?!

Tenant Placement is a service that allows landlords to leave the stress of filling vacancies behind.
zMobvra provides landlords, investors and property manager's a system to occupy vacancies with qualified tenants Faster, Cheaper, Easier
zMobvra takes the hassle out of the rental process from searching for tenants to move-in inspections.

Reason: I'm extending the deadline because I want to give other designers an opportunity to submit and I have a couple designs that I'm awaiting current designers to resubmit some designs.

```html
<!DOCTYPE html>
<html lang="en">
<head>
<meta charset="utf-8">
<title>zMobvra – Tenant Placement</title>
<link rel="stylesheet" href="https://fonts.googleapis.com/css2?family=Oswald:wght@500;600;700&display=swap">
<style>
  :root {
    --green-light: #7cc92f;
    --green-mid: #52a81d;
    --green-dark: #2c7d0c;
    --orange-light: #ffb347;
    --orange: #f58a1f;
    --orange-dark: #d9560f;
    --white: #ffffff;
    --brand-green: #6cb52d;
    --photo-light: #f3f5f6;
    --photo-mid: #dde1e4;
    --photo-deep: #aeb5bb;
  }
  html, body {
    margin: 0;
    padding: 0;
    overflow: hidden;
    background: var(--white);
  }
  .ad {
    position: relative;
    width: 1200px;
    height: 840px;
    overflow: hidden;
    font-family: "Oswald", "Arial Narrow", sans-serif;
  }
  .office-photo {
    position: absolute;
    left: 520px;
    top: 0;
    width: 680px;
    height: 600px;
    background: linear-gradient(160deg, var(--photo-light) 0%, var(--photo-mid) 55%, var(--photo-deep) 100%);
  }
  .panel-shape {
    position: absolute;
    inset: 0;
  }
  .headline {
    position: absolute;
    left: 20px;
    top: 79px;
    width: 580px;
    margin: 0;
    text-align center;
    text-align: center;
    font-weight: 700;
    font-size: 88px;
    line-height: 1;
    letter-spacing: 0;
    white-space: nowrap;
    background: linear-gradient(180deg, var(--orange-light) 0%, var(--orange) 55%, var(--orange-dark) 100%);
    -webkit-background-clip: text;
    background-clip: text;
    color: transparent;
  }
  .headline-rule {
    position: absolute;
    left: 80px;
    top: 240px;
    width: 460px;
    height: 2px;
    background: linear-gradient(90deg, rgba(255,255,255,0), rgba(255,255,255,0.55), rgba(255,255,255,0));
  }
  .pitch {
    position: absolute;
    left: 20px;
    top: 256px;
    width: 520px;
    margin: 0;
    text-align: center;
    color: var(--white);
    font-weight: 600;
    font-size: 78px;
    line-height: 114px;
    white-space: nowrap;
  }
  .cta {
    position: absolute;
    left: 89px;
    top: 690px;
    width: 338px;
    height: 100px;
    display: flex;
    align-items: center;
    box-sizing: border-box;
    border-radius: 10px;
    border: 3px solid var(--orange-dark);
    background: linear-gradient(180deg, var(--orange-light) 0%, var(--orange) 50%, var(--orange-dark) 100%);
    color: var(--white);
    text-decoration: none;
    font-weight: 500;
    font-size: 46px;
    letter-spacing: 1px;
  }
  .cta-label {
    flex: 1;
    text-align: center;
  }
  .cta-arrow {
    width: 72px;
    height: 100%;
    display: flex;
    align-items: center;
    justify-content: center;
    border-left: 2px solid rgba(255,255,255,0.5);
  }
  .brand {
    position: absolute;
    left: 557px;
    top: 600px;
    width: 643px;
    height: 240px;
    background: var(--white);
    display: flex;
    align-items: center;
    justify-content: center;
    gap: 18px;
  }
  .brand-mark {
    width: 22px;
    height: 22px;
    background: var(--brand-green);
  }
  .brand-name {
    color: var(--brand-green);
    font-weight: 500;
    font-size: 48px;
    letter-spacing: 3px;
  }
</style>
</head>
<body>
<main class="ad">
  <div class="office-photo" role="img" aria-label="Photo of a smiling businesswoman in a dark suit in a bright office with colleagues at a table behind her"></div>

  <svg class="panel-shape" width="1200" height="840" viewBox="0 0 1200 840" aria-hidden="true">
    <defs>
      <radialGradient id="panel-green" cx="35%" cy="40%" r="70%">
        <stop offset="0" stop-color="#7cc92f"/>
        <stop offset="0.55" stop-color="#52a81d"/>
        <stop offset="1" stop-color="#2c7d0c"/>
      </radialGradient>
    </defs>
    <path d="M0 0 H790 Q 610 420 570 840 H0 Z" fill="#ffffff"/>
    <path d="M0 0 H775 Q 596 420 557 840 H0 Z" fill="url(#panel-green)"/>
  </svg>

  <h1 class="headline">NEED TENANTS?!</h1>
  <div class="headline-rule"></div>
  <p class="pitch">Fill your vacancy<br>Faster, Easier,<br>Cheaper</p>

  <a class="cta" href="#">
    <span class="cta-label">LEARN MORE</span>
    <span class="cta-arrow">
      <svg width="26" height="34" viewBox="0 0 26 34" aria-hidden="true">
        <path d="M5 3 L21 17 L5 31" fill="none" stroke="#ffffff" stroke-width="6" stroke-linejoin="round" stroke-linecap="round"/>
      </svg>
    </span>
  </a>

  <div class="brand">
    <span class="brand-mark"></span>
    <span class="brand-name">zMobvra</span>
  </div>
</main>
</body>
</html>
```